Business Card Design Project

Logo, Phone Number, slogan, must be included on front of card. Services must be listed: Lawn Service, Fertilization, Pool Service, Pressure Washing. and a space to "write in" salesmans name.
Slogan "Your Everything Outside Company"
Phone: 602-417-3859
Email: brightacreyard@mailnest.net
Looking for a bold yet simple design to enforce brand recognition.

Target Market(s)

Middle to upper class US homeowners

Industry/Entity Type

Business

Requirements
Must have
• Logo, Phone, and Slogan on front
Should not have
• cluttered background

Files

```html
<!DOCTYPE html>
<html lang="en">
<head>
<meta charset="utf-8">
<title>Brightacre Yard – Business Card</title>
<link href="https://fonts.googleapis.com/css2?family=Roboto:wght@300;400;500;700&display=swap" rel="stylesheet">
<style>
  :root{
    --page:#eeeeee;
    --card:#ffffff;
    --brand-blue:#1b5e96;
    --bright-blue:#1e9ac4;
    --deep-blue:#165a92;
    --leaf:#6aa43a;
    --slate:#5f6367;
    --muted:#8a8d90;
    --rule:#e6e6e6;
  }
  *{margin:0;padding:0;box-sizing:border-box}
  html,body{width:1200px;height:1000px;overflow:hidden}
  body{background:var(--page);font-family:"Roboto",Arial,sans-serif;position:relative}

  .card{position:absolute;background:var(--card);box-shadow:0 2px 6px rgba(0,0,0,.18)}
  .card--front{left:288px;top:122px;width:640px;height:366px;display:flex;align-items:center;justify-content:center}
  .card--back{left:285px;top:516px;width:643px;height:367px;display:flex}

  .wordmark{color:var(--brand-blue);font-weight:700;text-align:center;line-height:1;letter-spacing:1px;display:flex;align-items:center;gap:12px}
  .wordmark__dot{width:22px;height:22px;border-radius:50%;background:var(--brand-blue);flex:none}
  .card--front .wordmark{font-size:40px}

  .back__info{width:325px;position:relative;text-align:center}
  .back__info .wordmark{position:absolute;left:0;right:0;top:92px;justify-content:center;font-size:27px;gap:9px}
  .back__info .wordmark__dot{width:16px;height:16px}
  .back__rule{position:absolute;left:35px;right:35px;top:206px;height:1px;background:var(--rule)}
  .slogan{position:absolute;left:0;right:0;top:224px;font-size:20px;line-height:25px;color:var(--muted);font-weight:300;letter-spacing:.2px}
  .slogan strong{font-weight:500}
  .slogan .blue{color:var(--brand-blue)}
  .slogan .green{color:var(--leaf)}
  .phone{position:absolute;left:0;right:0;top:293px;font-size:22px;font-weight:700;color:var(--muted);display:flex;justify-content:center;align-items:center;gap:6px}
  .email{position:absolute;left:0;right:0;top:324px;font-size:15px;color:var(--muted)}

  .back__services{flex:1;background:linear-gradient(90deg,var(--deep-blue),var(--bright-blue));position:relative;color:#fff}
  .services{list-style:none;position:absolute;left:35px;top:34px}
  .services li{display:flex;align-items:flex-start;gap:11px;font-size:22px;line-height:35.5px;font-weight:400}
  .services svg{margin-top:5px;flex:none}
  .salesman-label{position:absolute;left:39px;top:248px;font-size:18px}
  .salesman-field{position:absolute;left:37px;top:292px;width:246px;height:42px;background:#fff;border-radius:8px;display:flex;align-items:center;padding-left:11px}
</style>
</head>
<body>

<section class="card card--front">
  <div class="wordmark"><span class="wordmark__dot"></span>BRIGHTACRE YARD</div>
</section>

<section class="card card--back">
  <div class="back__info">
    <div class="wordmark"><span class="wordmark__dot"></span>BRIGHTACRE YARD</div>
    <div class="back__rule"></div>
    <p class="slogan">YOUR <strong class="blue">EVERYTHING</strong><br><strong class="green">OUTSIDE</strong> COMPANY</p>
    <p class="phone">
      <svg width="20" height="16" viewBox="0 0 20 16" aria-hidden="true"><path d="M2 5c0-3 16-3 16 0v2h-4V5H6v2H2z M4 8h12l2 7H2z" fill="#8a8d90"/><circle cx="10" cy="11.5" r="2" fill="#fff"/></svg>
      602-417-3859
    </p>
    <p class="email">brightacreyard@mailnest.net</p>
  </div>

  <div class="back__services">
    <ul class="services">
      <li><svg width="26" height="22" viewBox="0 0 26 22" aria-hidden="true"><path d="M1 11l4-3 5 6L23 1l2 3L10 21z" fill="#7cc04a"/></svg>LAWN SERVICE</li>
      <li><svg width="26" height="22" viewBox="0 0 26 22" aria-hidden="true"><path d="M1 11l4-3 5 6L23 1l2 3L10 21z" fill="#7cc04a"/></svg>FERTILIZATION</li>
      <li><svg width="26" height="22" viewBox="0 0 26 22" aria-hidden="true"><path d="M1 11l4-3 5 6L23 1l2 3L10 21z" fill="#7cc04a"/></svg>POOL SERVICE</li>
      <li><svg width="26" height="22" viewBox="0 0 26 22" aria-hidden="true"><path d="M1 11l4-3 5 6L23 1l2 3L10 21z" fill="#7cc04a"/></svg>PRESSURE<br>WASHING</li>
    </ul>
    <p class="salesman-label">Your salesman:</p>
    <div class="salesman-field">
      <svg width="22" height="22" viewBox="0 0 22 22" aria-hidden="true"><path d="M3 19l1-5L15 3l4 4L8 18z" fill="#6aa43a"/><path d="M3 19l1-5 4 4z" fill="#4d7d28"/></svg>
    </div>
  </div>
</section>

</body>
</html>
```